Employee Wellbeing Model Graphic Design

A visual/graphic representation of our Employee Wellbeing model.
Our model is a combination of the Ngā Kiri Rehu Pona model of health and wellbeing and the wellbeing continuum.
We would like the visual to be on one page. The design should be modern and simple.
The powerpoint attached shows the information we are wanting to share with our employees about our wellbeing programme.

Target Market(s)

Our employees

Industry/Entity Type

Event Management

Font styles to use
Sans Serif
Other font styles liked:
• calibri light

Colors
00AB8E
00BBA5
67D7C9
C6EFE9
E9F9F6

```html
<!DOCTYPE html>
<html lang="en">
<head>
<meta charset="utf-8">
<title>Integrated Employee Wellbeing</title>
<link rel="stylesheet" href="https://fonts.googleapis.com/css2?family=Inter:wght@500&family=Montserrat:wght@600&display=swap">
<style>
  :root {
    --teal-deep: #063b38;
    --teal-night: #0a2f2d;
    --teal-dark: #0d5550;
    --teal: #00ab8e;
    --teal-bright: #00bba5;
    --teal-soft: #67d7c9;
    --teal-pale: #c6efe9;
    --teal-mist: #e9f9f6;
    --line: rgba(255,255,255,0.92);
    --line-soft: rgba(255,255,255,0.5);
    --ink: #ffffff;
  }
  * { margin: 0; padding: 0; box-sizing: border-box; }
  html, body { width: 1200px; height: 900px; overflow: hidden; background: var(--teal-night); }
  .canvas { position: relative; width: 1200px; height: 900px; overflow: hidden; }
  .quadrant { position: absolute; width: 600px; height: 450px; }
  .quadrant--physical { left: 0; top: 0; background: linear-gradient(135deg, #1f8277 0%, var(--teal-dark) 100%); }
  .quadrant--family { left: 600px; top: 0; background: linear-gradient(200deg, var(--teal) 0%, var(--teal-dark) 55%, var(--teal-deep) 100%); }
  .quadrant--mental { left: 0; top: 450px; background: linear-gradient(160deg, var(--teal-night) 0%, #082624 100%); }
  .quadrant--spiritual { left: 600px; top: 450px; background: linear-gradient(140deg, var(--teal-dark) 0%, var(--teal) 45%, var(--teal-bright) 75%, var(--teal-soft) 100%); }
  .model { position: absolute; inset: 0; width: 1200px; height: 900px; }
  .dimension-label {
    position: absolute;
    font-family: "Montserrat", sans-serif;
    font-weight: 600;
    font-size: 14px;
    line-height: 1.3;
    letter-spacing: 0.04em;
    color: var(--ink);
    text-align: center;
    white-space: nowrap;
    transform: translate(-50%, -50%);
  }
  .dimension-label--physical { left: 190px; top: 250px; }
  .dimension-label--family { left: 992px; top: 254px; }
  .dimension-label--mental { left: 275px; top: 656px; }
  .dimension-label--spiritual { left: 955px; top: 656px; }
  .core-title {
    position: absolute;
    left: 600px; top: 450px;
    transform: translate(-50%, -50%);
    font-family: "Inter", sans-serif;
    font-weight: 500;
    font-size: 21px;
    line-height: 1.3;
    color: var(--ink);
    text-align: center;
    width: 170px;
  }
</style>
</head>
<body>
<div class="canvas">
  <div class="quadrant quadrant--physical"></div>
  <div class="quadrant quadrant--family"></div>
  <div class="quadrant quadrant--mental"></div>
  <div class="quadrant quadrant--spiritual"></div>

  <svg class="model" viewBox="0 0 1152 864" xmlns="http://www.w3.org/2000/svg">
    <defs>
      <symbol id="icon-heart" viewBox="-10 -10 20 20"><path d="M0 7 L-7 0 A3.6 3.6 0 0 1 0 -5 A3.6 3.6 0 0 1 7 0 Z" fill="none" stroke="#fff" stroke-width="1.5" stroke-linejoin="round"/></symbol>
      <symbol id="icon-tick" viewBox="-10 -10 20 20"><path d="M-6 0 L-2 5 L7 -5" fill="none" stroke="#fff" stroke-width="1.8" stroke-linecap="round" stroke-linejoin="round"/></symbol>
      <symbol id="icon-arrow" viewBox="-10 -10 20 20"><path d="M-7 0 H6 M1 -5 L6 0 L1 5" fill="none" stroke="#fff" stroke-width="1.6" stroke-linecap="round" stroke-linejoin="round"/></symbol>
      <symbol id="icon-calendar" viewBox="-10 -10 20 20"><g fill="none" stroke="#fff" stroke-width="1.4"><rect x="-7" y="-6" width="14" height="13" rx="1.5"/><path d="M-7 -2 H7 M-3 -8 V-4 M3 -8 V-4"/></g></symbol>
      <symbol id="icon-clock" viewBox="-10 -10 20 20"><g fill="none" stroke="#fff" stroke-width="1.4" stroke-linecap="round"><circle r="7"/><path d="M0 -4 V0 L3 2"/></g></symbol>
      <symbol id="icon-pin" viewBox="-10 -10 20 20"><g fill="none" stroke="#fff" stroke-width="1.4"><path d="M0 8 C-5 2 -6 -1 -6 -2 A6 6 0 0 1 6 -2 C6 -1 5 2 0 8 Z"/><circle cy="-2" r="2"/></g></symbol>
      <symbol id="icon-star" viewBox="-10 -10 20 20"><path d="M0 -7 L2 -2 L7 -2 L3 1.5 L4.5 7 L0 3.5 L-4.5 7 L-3 1.5 L-7 -2 L-2 -2 Z" fill="none" stroke="#fff" stroke-width="1.3" stroke-linejoin="round"/></symbol>
      <symbol id="icon-home" viewBox="-10 -10 20 20"><path d="M-7 0 L0 -6 L7 0 M-5 -1 V7 H5 V-1 M-1.5 7 V3 H1.5 V7" fill="none" stroke="#fff" stroke-width="1.4" stroke-linejoin="round"/></symbol>
      <symbol id="icon-phone" viewBox="-10 -10 20 20"><g fill="none" stroke="#fff" stroke-width="1.4"><rect x="-4.5" y="-7.5" width="9" height="15" rx="1.5"/><path d="M-1.5 5 H1.5"/></g></symbol>
    </defs>

    <g class="continuum-rings" fill="none" stroke="var(--line-soft)" stroke-width="1">
      <circle cx="576" cy="432" r="125"/><circle cx="576" cy="432" r="137"/>
      <circle cx="576" cy="432" r="149"/><circle cx="576" cy="432" r="161"/>
      <circle cx="576" cy="432" r="173"/><circle cx="576" cy="432" r="185"/>
      <circle cx="576" cy="432" r="197"/><circle cx="576" cy="432" r="209"/>
      <circle cx="576" cy="432" r="221"/><circle cx="576" cy="432" r="233"/>
    </g>
    <g class="spokes" stroke="var(--line)" stroke-width="3">
      <line x1="576" y1="252" x2="576" y2="612"/>
      <line x1="379" y1="432" x2="773" y2="432"/>
    </g>
    <circle class="core" cx="576" cy="432" r="95" fill="#0b4843" stroke="var(--line)" stroke-width="3"/>

    <g class="dimension-nodes" stroke="var(--line)" stroke-width="3">
      <circle cx="576" cy="196" r="57" fill="#0d4f4a"/>
      <circle cx="322" cy="430" r="57" fill="#16685f"/>
      <circle cx="830" cy="430" r="57" fill="#07756a"/>
      <circle cx="576" cy="668" r="57" fill="#0b4a45"/>
    </g>
    <g class="dimension-nodes-art">
      <circle cx="576" cy="196" r="42" fill="#1b6a62" role="img" aria-label="Line illustration for mental wellbeing"/>
      <circle cx="322" cy="430" r="42" fill="#26857a" role="img" aria-label="Line illustration of people for physical wellbeing"/>
      <circle cx="830" cy="430" r="42" fill="#1e958a" role="img" aria-label="Line illustration of a family group"/>
      <circle cx="576" cy="668" r="42" fill="#176b63" role="img" aria-label="Line illustration of a connected community"/>
    </g>

    <g class="activity-icons" fill="rgba(255,255,255,0.08)" stroke="var(--line)" stroke-width="1.5">
      <g aria-label="Physical activity icons">
        <g transform="translate(536 65)"><circle r="20"/><use href="#icon-heart" x="-11" y="-11" width="22" height="22"/></g>
        <g transform="translate(475 95)"><circle r="20"/><use href="#icon-clock" x="-11" y="-11" width="22" height="22"/></g>
        <g transform="translate(430 140)"><circle r="20"/><use href="#icon-tick" x="-11" y="-11" width="22" height="22"/></g>
        <g transform="translate(490 145)"><circle r="20"/><use href="#icon-star" x="-11" y="-11" width="22" height="22"/></g>
        <g transform="translate(535 112)"><circle r="20"/><use href="#icon-arrow" x="-11" y="-11" width="22" height="22"/></g>
        <g transform="translate(418 195)"><circle r="20"/><use href="#icon-pin" x="-11" y="-11" width="22" height="22"/></g>
        <g transform="translate(472 190)"><circle r="20"/><use href="#icon-calendar" x="-11" y="-11" width="22" height="22"/></g>
      </g>
      <g aria-label="Mental wellbeing icons">
        <g transform="translate(617 65)"><circle r="20"/><use href="#icon-calendar" x="-11" y="-11" width="22" height="22"/></g>
        <g transform="translate(676 95)"><circle r="20"/><use href="#icon-star" x="-11" y="-11" width="22" height="22"/></g>
        <g transform="translate(722 140)"><circle r="20"/><use href="#icon-heart" x="-11" y="-11" width="22" height="22"/></g>
        <g transform="translate(667 150)"><circle r="20"/><use href="#icon-clock" x="-11" y="-11" width="22" height="22"/></g>
        <g transform="translate(617 112)"><circle r="20"/><use href="#icon-phone" x="-11" y="-11" width="22" height="22"/></g>
        <g transform="translate(730 200)"><circle r="20"/><use href="#icon-tick" x="-11" y="-11" width="22" height="22"/></g>
        <g transform="translate(668 202)"><circle r="20"/><use href="#icon-home" x="-11" y="-11" width="22" height="22"/></g>
      </g>
      <g aria-label="Fitness and health icons">
        <g transform="translate(255 300)"><circle r="20"/><use href="#icon-arrow" x="-11" y="-11" width="22" height="22"/></g>
        <g transform="translate(318 290)"><circle r="20"/><use href="#icon-heart" x="-11" y="-11" width="22" height="22"/></g>
        <g transform="translate(215 340)"><circle r="20"/><use href="#icon-star" x="-11" y="-11" width="22" height="22"/></g>
        <g transform="translate(310 340)"><circle r="20"/><use href="#icon-clock" x="-11" y="-11" width="22" height="22"/></g>
        <g transform="translate(270 355)"><circle r="20"/><use href="#icon-calendar" x="-11" y="-11" width="22" height="22"/></g>
        <g transform="translate(190 390)"><circle r="20"/><use href="#icon-phone" x="-11" y="-11" width="22" height="22"/></g>
        <g transform="translate(245 395)"><circle r="20"/><use href="#icon-tick" x="-11" y="-11" width="22" height="22"/></g>
      </g>
      <g aria-label="Mind and balance icons">
        <g transform="translate(185 470)"><circle r="20"/><use href="#icon-pin" x="-11" y="-11" width="22" height="22"/></g>
        <g transform="translate(240 465)"><circle r="20"/><use href="#icon-clock" x="-11" y="-11" width="22" height="22"/></g>
        <g transform="translate(215 520)"><circle r="20"/><use href="#icon-star" x="-11" y="-11" width="22" height="22"/></g>
        <g transform="translate(305 525)"><circle r="20"/><use href="#icon-heart" x="-11" y="-11" width="22" height="22"/></g>
        <g transform="translate(255 570)"><circle r="20"/><use href="#icon-arrow" x="-11" y="-11" width="22" height="22"/></g>
        <g transform="translate(315 570)"><circle r="20"/><use href="#icon-calendar" x="-11" y="-11" width="22" height="22"/></g>
        <g transform="translate(265 515)"><circle r="20"/><use href="#icon-tick" x="-11" y="-11" width="22" height="22"/></g>
      </g>
      <g aria-label="Family time icons">
        <g transform="translate(830 290)"><circle r="20"/><use href="#icon-calendar" x="-11" y="-11" width="22" height="22"/></g>
        <g transform="translate(890 300)"><circle r="20"/><use href="#icon-home" x="-11" y="-11" width="22" height="22"/></g>
        <g transform="translate(840 340)"><circle r="20"/><use href="#icon-phone" x="-11" y="-11" width="22" height="22"/></g>
        <g transform="translate(940 345)"><circle r="20"/><use href="#icon-heart" x="-11" y="-11" width="22" height="22"/></g>
        <g transform="translate(890 355)"><circle r="20"/><use href="#icon-clock" x="-11" y="-11" width="22" height="22"/></g>
        <g transform="translate(960 395)"><circle r="20"/><use href="#icon-star" x="-11" y="-11" width="22" height="22"/></g>
        <g transform="translate(910 395)"><circle r="20"/><use href="#icon-pin" x="-11" y="-11" width="22" height="22"/></g>
      </g>
      <g aria-label="Spiritual practice icons">
        <g transform="translate(965 465)"><circle r="20"/><use href="#icon-star" x="-11" y="-11" width="22" height="22"/></g>
        <g transform="translate(910 465)"><circle r="20"/><use href="#icon-heart" x="-11" y="-11" width="22" height="22"/></g>
        <g transform="translate(940 520)"><circle r="20"/><use href="#icon-pin" x="-11" y="-11" width="22" height="22"/></g>
        <g transform="translate(850 525)"><circle r="20"/><use href="#icon-home" x="-11" y="-11" width="22" height="22"/></g>
        <g transform="translate(890 565)"><circle r="20"/><use href="#icon-clock" x="-11" y="-11" width="22" height="22"/></g>
        <g transform="translate(835 570)"><circle r="20"/><use href="#icon-tick" x="-11" y="-11" width="22" height="22"/></g>
        <g transform="translate(880 515)"><circle r="20"/><use href="#icon-arrow" x="-11" y="-11" width="22" height="22"/></g>
      </g>
      <g aria-label="Community and social icons">
        <g transform="translate(420 655)"><circle r="20"/><use href="#icon-phone" x="-11" y="-11" width="22" height="22"/></g>
        <g transform="translate(470 680)"><circle r="20"/><use href="#icon-heart" x="-11" y="-11" width="22" height="22"/></g>
        <g transform="translate(420 715)"><circle r="20"/><use href="#icon-calendar" x="-11" y="-11" width="22" height="22"/></g>
        <g transform="translate(490 720)"><circle r="20"/><use href="#icon-home" x="-11" y="-11" width="22" height="22"/></g>
        <g transform="translate(540 740)"><circle r="20"/><use href="#icon-star" x="-11" y="-11" width="22" height="22"/></g>
        <g transform="translate(470 765)"><circle r="20"/><use href="#icon-pin" x="-11" y="-11" width="22" height="22"/></g>
        <g transform="translate(530 790)"><circle r="20"/><use href="#icon-tick" x="-11" y="-11" width="22" height="22"/></g>
      </g>
      <g aria-label="Reflection and connection icons">
        <g transform="translate(732 655)"><circle r="20"/><use href="#icon-clock" x="-11" y="-11" width="22" height="22"/></g>
        <g transform="translate(680 675)"><circle r="20"/><use href="#icon-star" x="-11" y="-11" width="22" height="22"/></g>
        <g transform="translate(732 715)"><circle r="20"/><use href="#icon-heart" x="-11" y="-11" width="22" height="22"/></g>
        <g transform="translate(665 720)"><circle r="20"/><use href="#icon-arrow" x="-11" y="-11" width="22" height="22"/></g>
        <g transform="translate(612 740)"><circle r="20"/><use href="#icon-tick" x="-11" y="-11" width="22" height="22"/></g>
        <g transform="translate(675 770)"><circle r="20"/><use href="#icon-calendar" x="-11" y="-11" width="22" height="22"/></g>
        <g transform="translate(617 790)"><circle r="20"/><use href="#icon-home" x="-11" y="-11" width="22" height="22"/></g>
      </g>
    </g>
  </svg>

  <p class="dimension-label dimension-label--physical">PHYSICAL<br>WELLBEING.</p>
  <p class="dimension-label dimension-label--family">FAMILY<br>WELLBEING.</p>
  <p class="dimension-label dimension-label--mental">MENTAL<br>WELLBEING.</p>
  <p class="dimension-label dimension-label--spiritual">SPIRITUAL<br>WELLBEING.</p>

  <h1 class="core-title">Integrated Employee Wellbeing.</h1>
</div>
</body>
</html>
```